Need innovative card design for tech start up

We are a Santa Monica based marketing analytics software start up called Brightwell Metrics. We're launching a platform that will help advertisers better measure and optimize their marketing spend by using advanced algorithmic analytic. While our subject matter is complicated, we want to convey simple, clean, curated. We also want to stand out - ad tech is a sea of sameness and we need to have some individuality. We have an established color palette and would like to see a design we could print in each tone (teal, tangerine, grey), but it doesn't require the card to be monochromatic. The font used is DENSE.

Marketing

```html
<!DOCTYPE html>
<html lang="en">
<head>
<meta charset="utf-8">
<title>Brightwell Metrics – Business Card</title>
<link href="https://fonts.googleapis.com/css2?family=Oswald:wght@300&family=Open+Sans:wght@400;600&display=swap" rel="stylesheet">
<style>
  :root {
    --backdrop: #e9e7e3;
    --card: #ffffff;
    --brand-grey: #9a9a9a;
    --mark-grey: #c4c4c4;
    --faint-grey: #f1f1f1;
    --ink: #2e2e2e;
    --ink-soft: #6a6a6a;
    --accent-blue: #3f9ee0;
  }
  * { margin: 0; padding: 0; box-sizing: border-box; }
  html, body {
    width: 1200px; height: 918px; overflow: hidden;
    background: var(--backdrop);
  }
  .canvas {
    position: relative; width: 1200px; height: 918px;
  }
  .card {
    position: absolute;
    background: var(--card);
    overflow: hidden;
    box-shadow: 0 6px 18px rgba(0,0,0,0.12);
  }

  /* Front side: landscape */
  .card-front {
    left: 130px; top: 299px; width: 560px; height: 320px;
  }
  .front-mark {
    position: absolute; left: 50%; top: 52px;
    width: 110px; height: 110px; margin-left: -55px;
    border-radius: 50%; background: var(--mark-grey);
  }
  .front-name {
    position: absolute; left: 0; right: 0; top: 178px;
    text-align: center;
    font-family: "Oswald", sans-serif; font-weight: 300;
    font-size: 44px; letter-spacing: 0.5px; text-transform: uppercase;
    color: var(--brand-grey);
  }
  .front-band {
    position: absolute; left: 0; right: 0; bottom: 0; height: 16px;
    background: linear-gradient(to right, rgba(63,158,224,0) 40%, var(--accent-blue) 100%);
  }

  /* Back side: portrait */
  .card-back {
    left: 750px; top: 179px; width: 320px; height: 560px;
  }
  .back-band {
    position: absolute; left: 0; right: 0; top: 0; height: 14px;
    background: linear-gradient(to left, var(--accent-blue) 0%, rgba(63,158,224,0) 70%);
  }
  .back-name {
    position: absolute; left: 26px; top: 30px;
    font-family: "Oswald", sans-serif; font-weight: 300;
    font-size: 28px; letter-spacing: 0.5px; text-transform: uppercase;
    color: var(--brand-grey);
  }
  .back-watermark {
    position: absolute; left: 120px; top: 230px;
    width: 230px; height: 230px; border-radius: 50%;
    background: var(--faint-grey);
  }
  .contact {
    position: absolute; left: 26px; top: 150px; right: 20px;
    font-family: "Open Sans", sans-serif; color: var(--ink);
  }
  .contact-person {
    font-size: 22px; font-weight: 400; line-height: 1.1;
  }
  .contact-role {
    font-size: 10px; color: var(--ink-soft); margin-bottom: 20px;
  }
  .contact-lines {
    list-style: none;
    font-size: 14px; font-weight: 600; line-height: 1.3;
  }
</style>
</head>
<body>
<main class="canvas">
  <section class="card card-front" aria-label="Card front">
    <div class="front-mark"></div>
    <h1 class="front-name">Brightwell Metrics</h1>
    <div class="front-band"></div>
  </section>

  <section class="card card-back" aria-label="Card back">
    <div class="back-band"></div>
    <div class="back-watermark"></div>
    <p class="back-name">Brightwell Metrics</p>
    <div class="contact">
      <p class="contact-person">Dana Whitlock</p>
      <p class="contact-role">Founder/CEO</p>
      <ul class="contact-lines">
        <li>1180 Harbor Crest suite 300</li>
        <li>Santa Monica, CA 90401</li>
        <li>Off: 310-555-0142 x101</li>
        <li>Mob: 310-555-0187</li>
        <li>dana@brightwellmetrics.com</li>
        <li>www.brightwellmetrics.com</li>
      </ul>
    </div>
  </section>
</main>
</body>
</html>
```